Stationary Set Rebrand for Brenvik

We are a Canadian Distribution and Service Company that was established in 1969. Over the past 5 decades we have expanded our business and have warehouses across Canada. We specialize in adhesive tapes, adhesives, films, safety, warehouse, shipping, janitorial and packaging supplies.

We have updated our logo design and would like a new corporate branding identity that includes a new fresh Stationary Set (Business Cards, Letterhead, Letterhead MS Word, Envelope, Presentation Folders, Email Signatures, Notepad Covers, etc.)

Target Market(s)

Industrial Business Sector

Font styles to use
Sans Serif

Colors
0054AA
0677BA
7BADD7
CADEEF
E8F1F8
0094D4
00A9DD
6FCCEA
C7EBF8
E9F6FB
00AB8E
00BBA5
67D7C9
C6EFE9
E9F9F6
EB3D1F
EC4F4E
F09395
F8D3D4
FCEDEE

Requirements
Should not have
• Colors not too light, darker colours preferred

```html
<!DOCTYPE html>
<html lang="en">
<head>
<meta charset="utf-8">
<title>Brenvik Stationery — Folder and Notebooks</title>
<link href="https://fonts.googleapis.com/css2?family=Roboto:wght@400;500;900&display=swap" rel="stylesheet">
<style>
  :root {
    --backdrop: #eeeeee;
    --paper: #f7f7f7;
    --ink: #1a1a1a;
    --panel-dark: #141414;
    --panel-dark-edge: #242424;
    --accent-red: #d8231a;
    --muted: #8a8a8a;
    --ring: #9a9a9a;
  }
  * { box-sizing: border-box; margin: 0; padding: 0; }
  html, body { width: 811px; height: 1200px; overflow: hidden; }
  body {
    background: var(--backdrop);
    font-family: "Roboto", Arial, sans-serif;
    color: var(--ink);
    position: relative;
  }

  /* Presentation folder spread */
  .folder {
    position: absolute;
    left: 66px; top: 70px;
    width: 680px; height: 450px;
    display: flex;
    box-shadow: 0 10px 24px rgba(0,0,0,0.18);
  }
  .folder-back {
    width: 50%; height: 100%;
    background: linear-gradient(160deg, var(--panel-dark-edge), var(--panel-dark));
    position: relative;
  }
  .folder-front {
    width: 50%; height: 100%;
    background: var(--paper);
    position: relative;
  }

  /* Wordmark */
  .wordmark { display: inline-block; }
  .wordmark-name {
    display: block;
    font-weight: 900;
    letter-spacing: -0.5px;
    line-height: 1;
    color: var(--ink);
  }
  .wordmark-tagline {
    display: block;
    font-weight: 500;
    color: var(--ink);
    white-space: nowrap;
  }
  .wordmark--light .wordmark-name,
  .wordmark--light .wordmark-tagline { color: #ffffff; }

  .folder-front .wordmark { position: absolute; top: 36px; right: 40px; }
  .folder-front .wordmark-name { font-size: 30px; }
  .folder-front .wordmark-tagline { font-size: 9px; margin-top: 2px; }

  .folder-back .wordmark { position: absolute; left: 22px; bottom: 52px; }
  .folder-back .wordmark-name { font-size: 24px; }
  .folder-back .wordmark-tagline { font-size: 7px; margin-top: 2px; }

  .contact-list {
    position: absolute;
    left: 188px; bottom: 50px;
    list-style: none;
    font-size: 7px;
    color: #cfcfcf;
    line-height: 12px;
  }
  .contact-list li { display: flex; align-items: center; gap: 5px; }
  .contact-list svg { width: 7px; height: 7px; fill: #cfcfcf; }

  .leaf-mark {
    position: absolute;
    background: radial-gradient(circle at 50% 45%, #e0291e, #c41c14);
    border-radius: 46% 46% 40% 40%;
  }
  .folder-front .leaf-mark { width: 78px; height: 78px; left: 116px; bottom: 96px; }

  /* Notebooks */
  .notebook {
    position: absolute;
    top: 650px;
    width: 296px; height: 420px;
    box-shadow: 0 8px 18px rgba(0,0,0,0.16);
  }
  .notebook--front { left: 66px; background: var(--paper); }
  .notebook--back { left: 450px; background: linear-gradient(160deg, var(--panel-dark-edge), var(--panel-dark)); }

  .spiral {
    position: absolute;
    left: -6px; top: 10px; bottom: 10px;
    width: 16px;
    display: flex; flex-direction: column; justify-content: space-between;
  }
  .spiral span {
    display: block;
    width: 16px; height: 4px;
    border-radius: 2px;
    background: var(--ring);
  }

  .notebook--front .wordmark { position: absolute; top: 108px; left: 50%; transform: translateX(-50%); text-align: left; }
  .notebook--front .wordmark-name { font-size: 36px; }
  .notebook--front .wordmark-tagline { font-size: 10px; margin-top: 3px; }
  .notebook--front .leaf-mark { width: 64px; height: 64px; left: 116px; bottom: 32px; }
</style>
</head>
<body>

  <section class="folder" aria-label="Presentation folder">
    <div class="folder-back">
      <div class="wordmark wordmark--light">
        <span class="wordmark-name">Brenvik</span>
        <span class="wordmark-tagline">Tape and Packaging Specialists</span>
      </div>
      <ul class="contact-list">
        <li><svg viewBox="0 0 10 10"><path d="M2 1h2l1 2.5-1.2 1a6 6 0 0 0 2.7 2.7l1-1.2L10 7v2a1 1 0 0 1-1 1A9 9 0 0 1 0 2a1 1 0 0 1 1-1z"/></svg>+1 555 0142</li>
        <li><svg viewBox="0 0 10 10"><rect x="0" y="2" width="10" height="6"/></svg>info@brenvik.ca</li>
        <li><svg viewBox="0 0 10 10"><circle cx="5" cy="5" r="4.5"/></svg>www.brenvik.ca</li>
      </ul>
    </div>
    <div class="folder-front">
      <div class="wordmark">
        <span class="wordmark-name">Brenvik</span>
        <span class="wordmark-tagline">Tape and Packaging Specialists</span>
      </div>
      <div class="leaf-mark" role="img" aria-label="Red maple leaf emblem"></div>
    </div>
  </section>

  <section class="notebook notebook--front" aria-label="Notebook front cover">
    <div class="spiral">
      <span></span><span></span><span></span><span></span><span></span><span></span><span></span><span></span><span></span><span></span><span></span><span></span><span></span><span></span><span></span><span></span><span></span><span></span><span></span><span></span><span></span><span></span><span></span><span></span>
    </div>
    <div class="wordmark">
      <span class="wordmark-name">Brenvik</span>
      <span class="wordmark-tagline">Tape and Packaging Specialists</span>
    </div>
    <div class="leaf-mark" role="img" aria-label="Red maple leaf emblem"></div>
  </section>

  <section class="notebook notebook--back" aria-label="Notebook back cover">
    <div class="spiral">
      <span></span><span></span><span></span><span></span><span></span><span></span><span></span><span></span><span></span><span></span><span></span><span></span><span></span><span></span><span></span><span></span><span></span><span></span><span></span><span></span><span></span><span></span><span></span><span></span>
    </div>
  </section>

</body>
</html>
```